Business Card design for amazing new Dental Office

Please read this brief closely!

Our client is a modern new dental office/
They love their new logo.
Now it's time to create a business card for them.

It should be a two sided card:
Side one should have the logo and name and maybe a color background or design.
Side two should have all the contact information which is here:

Marcus Holloway, D.D.S
General and Cosmetic Dentistry
4187 W. Pinecrest Avenue
Ventura, CA 93011
(805) 912-4386
drmarcus@bluefernsmiles-example.com
www.bluefernsmiles-example.com

Feel free to arrange that info as you like and to style both sides of the card according to your creativity. This is a chance for you to show your design skills!

Client is open to font choices and is looking for a style that is amazing and premium. Colors can be selected from the logo, or any variation of those.

You will not win this contest with a less than beautiful card design so please feel free to make multiple submissions.

Logo files attached and please message me with any questions.
Thanks!

Target Market(s)

Families and Professionals seeking dental services

Industry/Entity Type

Dental

Contact Information for Business Card

Logo, style, contact info as per the brief

Font styles to use
Sans Serif

Requirements
Must have
• Client's logo and contact details as per brief
Nice to have
• Unique style reflecting high end dental clinic near the beach
Should not have
• Must not look like a template

```html
<!DOCTYPE html>
<html lang="en">
<head>
<meta charset="utf-8">
<title>Blue Fern Smiles – Business Card</title>
<link href="https://fonts.googleapis.com/css2?family=Roboto:wght@300;400;700&display=swap" rel="stylesheet">
<style>
  :root {
    --bg-top: #d4d4d4;
    --bg-bottom: #9c9c9c;
    --card-white: #ffffff;
    --ocean: #4bb3e4;
    --ocean-deep: #3ea6d8;
    --seafoam: #6cc4be;
    --sand: #e2a24a;
    --ink: #2b2b2b;
    --mist: #a9a9a9;
  }
  * { margin: 0; padding: 0; box-sizing: border-box; }
  html, body { width: 1200px; height: 788px; overflow: hidden; }
  body {
    background: linear-gradient(180deg, var(--bg-top), var(--bg-bottom));
    font-family: "Roboto", Arial, sans-serif;
    position: relative;
  }
  .card {
    position: absolute;
    top: 240px;
    width: 540px;
    height: 309px;
    border-radius: 18px;
    overflow: hidden;
    box-shadow: 0 14px 30px rgba(0,0,0,0.25);
  }
  .card--contact { left: 40px; background: var(--card-white); }
  .card--brand { left: 620px; background: var(--ocean); }

  .card__wave { position: absolute; inset: 0; width: 100%; height: 100%; }

  .brand-name {
    position: absolute;
    font-weight: 300;
    text-transform: uppercase;
    white-space: nowrap;
  }
  .card--contact .brand-name {
    left: 28px; top: 112px;
    width: 210px;
    text-align: center;
    color: var(--mist);
    font-size: 19px;
    letter-spacing: 4px;
    line-height: 1.5;
    white-space: normal;
  }
  .divider {
    position: absolute;
    left: 255px; top: 40px;
    width: 1px; height: 150px;
    background: var(--seafoam);
  }
  .contact {
    position: absolute;
    left: 272px; top: 34px;
    color: var(--ink);
    font-size: 12.5px;
    line-height: 1.45;
  }
  .contact__name {
    font-size: 21px;
    font-weight: 700;
    color: var(--seafoam);
    line-height: 1.1;
  }
  .contact__name .degree { color: var(--sand); font-size: 15px; }
  .contact__role { margin-bottom: 10px; }
  .contact__address { margin-bottom: 10px; }
  .contact__line { display: flex; align-items: center; gap: 7px; }
  .contact__line svg { width: 11px; height: 11px; flex: none; }

  .card--brand .brand-name {
    left: 0; right: 0; top: 136px;
    text-align: center;
    color: var(--card-white);
    font-size: 34px;
    letter-spacing: 7px;
  }
</style>
</head>
<body>

  <section class="card card--contact" aria-label="Card front with contact details">
    <svg class="card__wave" viewBox="0 0 540 309" preserveAspectRatio="none" aria-hidden="true">
      <path d="M0,280 C170,282 300,262 400,228 S515,196 540,192" fill="none" stroke="var(--seafoam)" stroke-width="3"/>
      <path d="M0,290 C180,290 300,270 405,238 S518,208 540,204 V309 H0 Z" fill="var(--ocean)"/>
    </svg>

    <p class="brand-name">Blue Fern Smiles</p>
    <div class="divider"></div>

    <div class="contact">
      <p class="contact__name">Marcus Holloway, <span class="degree">D.D.S</span></p>
      <p class="contact__role">General and Cosmetic Dentistry</p>
      <p class="contact__address">4187 W. Pinecrest Avenue<br>Ventura, CA 93011</p>
      <p class="contact__line">
        <svg viewBox="0 0 12 12"><path d="M2.5 1 L4.5 1 L5.2 3.6 L3.9 4.6 Q5 7 7.4 8.1 L8.4 6.8 L11 7.5 L11 9.5 Q11 11 9.5 11 Q1 10 1 2.5 Q1 1 2.5 1 Z" fill="var(--ocean)"/></svg>
        (805) 912-4386
      </p>
      <p class="contact__line">
        <svg viewBox="0 0 12 12"><rect x="0.5" y="2" width="11" height="8" rx="1" fill="var(--ocean)"/><path d="M0.8 2.5 L6 6.5 L11.2 2.5" fill="none" stroke="#fff" stroke-width="1"/></svg>
        drmarcus@bluefernsmiles-example.com
      </p>
      <p class="contact__line">
        <svg viewBox="0 0 12 12"><circle cx="6" cy="6" r="5.5" fill="var(--ocean)"/><ellipse cx="6" cy="6" rx="2.3" ry="5.2" fill="none" stroke="#fff" stroke-width="0.8"/><line x1="0.7" y1="6" x2="11.3" y2="6" stroke="#fff" stroke-width="0.8"/></svg>
        www.bluefernsmiles-example.com
      </p>
    </div>
  </section>

  <section class="card card--brand" aria-label="Card back with practice name">
    <svg class="card__wave" viewBox="0 0 540 309" preserveAspectRatio="none" aria-hidden="true">
      <path d="M0,60 C150,-10 330,20 540,110 V160 C330,70 150,40 0,110 Z" fill="var(--ocean-deep)" opacity="0.55"/>
      <path d="M0,200 C170,120 350,150 540,230 V290 C350,200 170,180 0,260 Z" fill="var(--ocean-deep)" opacity="0.55"/>
    </svg>
    <p class="brand-name">Blue Fern Smiles</p>
  </section>

</body>
</html>
```